Telepsychology Services

The company is called 'Vantor' and it is a telehealth business.

I would like a lego which has some sort of telecommunications or health feel to it, with the message 'New Technology. New You' incoproated in it.

On the front side of the side I would like the logo with the message 'Providing psychological services to 'hard-to-reach' individuals' printed in large font . I also need the message 'Real-time internet webcam conferencing' located on the front, along with the website address www.vantorclinic.com.au.

On the backside of the card, I would appreicate the following information

Suitable for individuals
•living in remote areas of Australia,
•who experience impairment which leaves them housebound,
•with limited time availability for appointments, and
•for whom high levels of confidentiliaty are important

Designed for individuals with minimal or no webcam experience

Benefits provided by specific private health insurers, ie KELM

All Psychologists registered with the Commonwealth Clinical Practice Licensing Bureau and members with the National Counselling Guild
Updates

Hi All,

Just a quick update.. I think I will prefer logos and busiiness cards that are relatively simple and understated. I am not a big fan of bright, multi colours and fancy designs. Just something clean, crisp, straightforward with a little colour ie blues and greens a good.

Also, for the back page, please keep in simple dot point form...

Thanks,

Mira

Industry/Entity Type

Telecommunications

Contact Information for Business Card

Vantor
www.vantorclinic.com.au

```html
<!DOCTYPE html>
<html lang="en">
<head>
<meta charset="utf-8">
<title>Vantor – Card Back</title>
<link rel="stylesheet" href="https://fonts.googleapis.com/css2?family=Open+Sans:wght@300;400&display=swap">
<style>
  :root {
    --page-bg: #ffffff;
    --card-teal: #55b2b6;
    --ink-light: #ffffff;
  }
  html, body {
    margin: 0;
    padding: 0;
    width: 1200px;
    height: 741px;
    overflow: hidden;
    background: var(--page-bg);
  }
  .canvas {
    position: relative;
    width: 1200px;
    height: 741px;
    font-family: "Open Sans", "Segoe UI", sans-serif;
    font-weight: 300;
    color: var(--ink-light);
  }
  .card-back {
    position: absolute;
    left: 25px;
    top: 38px;
    width: 1150px;
    height: 665px;
    background: var(--card-teal);
  }
  .suitability-title {
    position: absolute;
    left: 0;
    width: 1184px;
    top: 152px;
    margin: 0;
    text-align: center;
    font-size: 43px;
    font-weight: 300;
    line-height: 1;
  }
  .title-rule {
    position: absolute;
    left: 346px;
    top: 210px;
    width: 493px;
    height: 2px;
    background: var(--ink-light);
  }
  .suitability-list {
    position: absolute;
    left: 0;
    top: 238px;
    width: 1184px;
    margin: 0;
    padding: 0;
    list-style: none;
    text-align: center;
    font-size: 32px;
    line-height: 47.3px;
  }
  .footer-note {
    position: absolute;
    text-align: center;
    font-size: 29px;
    line-height: 38px;
    margin: 0;
  }
  .insurer-note {
    left: 60px;
    width: 500px;
    top: 559px;
  }
  .registration-note {
    left: 616px;
    width: 520px;
    top: 541px;
  }
  .footer-divider {
    position: absolute;
    left: 591px;
    top: 551px;
    width: 2px;
    height: 92px;
    background: var(--ink-light);
  }
</style>
</head>
<body>
  <main class="canvas">
    <section class="card-back">
    </section>
    <h1 class="suitability-title">Suitable for individuals</h1>
    <div class="title-rule"></div>
    <ul class="suitability-list">
      <li>{ living in remote areas of Australia }</li>
      <li>{ Housebound or experiencing impairment }</li>
      <li>{ with limited time availability for appointments }</li>
      <li>{ with high levels of confidentiliaty }</li>
      <li>{ with no webcam experience needed }</li>
    </ul>
    <p class="footer-note insurer-note">Benefits provided by specific<br>private health insurers, ie KELM.</p>
    <div class="footer-divider"></div>
    <p class="footer-note registration-note">All Psychologists registered with<br>the Commonwealth Clinical Practice<br>Licensing Bureau</p>
  </main>
</body>
</html>
```